Business Cards, Letterhead, Envelopes etc.
Need design that fits with tech saavy customers
Business Cards, Letterhead, Envelopes etc.  -
Creative Brief
Use specific fonts
Use same font or one that works with the logo
Cutting-Edge
Mark T. Derrow
President
418 Welland Avenue Palo Alto, CA 94306
mark@derfinco.com
derfinco.com
CA DRE: #00461738, NMLS: #517264
Need design for business cards, letterhead, #10 envelopes and mailing labels for package shipments.

```html
<!DOCTYPE html>
<html lang="en">
<head>
<meta charset="utf-8">
<title>Derfinco Stationery Suite</title>
<link href="https://fonts.googleapis.com/css2?family=Montserrat:wght@400;600;800&display=swap" rel="stylesheet">
<style>
  :root {
    --stage: #3b3b3b;
    --paper: #ffffff;
    --green: #6cb33f;
    --green-dark: #5ea233;
    --blue: #1b5fa9;
    --ink: #4a4a4a;
    --faint: #e6ebf2;
    --caption: #9a9a9a;
  }
  * { margin: 0; padding: 0; box-sizing: border-box; }
  html, body { width: 1200px; height: 310px; overflow: hidden; }
  body { background: var(--stage); font-family: "Montserrat", sans-serif; position: relative; color: var(--ink); }
  .piece { position: absolute; background: var(--paper); overflow: hidden; }
  .wordmark { font-weight: 800; color: var(--green); letter-spacing: 0.02em; white-space: nowrap; line-height: 1; }
  .wordmark.on-blue { color: var(--paper); }
  .caption { position: absolute; font-size: 5px; color: var(--caption); white-space: nowrap; }
  .contact { font-size: 3.6px; line-height: 1.4; color: var(--ink); white-space: nowrap; }

  .brand-block { position: absolute; left: 19px; top: 64px; width: 178px; }
  .brand-block .wordmark { font-size: 31px; }
  .brand-block .tagline { font-size: 6px; color: var(--caption); margin-top: 6px; text-align: center; }

  .card-wide { left: 19px; top: 124px; width: 106px; height: 30px; }
  .card-wide .wordmark { position: absolute; left: 8px; top: 9px; font-size: 10px; }
  .card-wide .stripe { position: absolute; left: 0; right: 0; bottom: 0; height: 4px; background: var(--blue); }

  .card-front { left: 19px; top: 214px; width: 111px; height: 43px; }
  .card-front .wordmark { position: absolute; left: 7px; top: 6px; font-size: 10px; }
  .card-front .person { position: absolute; left: 7px; top: 18px; }
  .card-front .person strong { display: block; font-size: 4.6px; line-height: 1.2; color: var(--blue); }
  .card-front .mark-dot { position: absolute; right: -10px; bottom: -10px; width: 30px; height: 30px; border-radius: 50%; background: var(--faint); }

  .card-back { left: 139px; top: 214px; width: 111px; height: 43px; background: var(--blue); }
  .card-back .wordmark { position: absolute; left: 0; right: 0; top: 15px; text-align: center; font-size: 12px; }

  .letterhead { top: 19px; width: 192px; height: 255px; }
  .letterhead.one { left: 264px; }
  .letterhead.two { left: 480px; }
  .letterhead .wordmark { position: absolute; left: 12px; top: 14px; font-size: 13px; }
  .letterhead .contact { position: absolute; right: 12px; top: 12px; text-align: right; }
  .letterhead .watermark { position: absolute; left: 50px; top: 70px; width: 92px; height: 92px; border-radius: 50%; background: var(--faint); }
  .letterhead .footer-rule { position: absolute; left: 0; right: 0; bottom: 8px; height: 3px; background: var(--blue); }
  .letterhead .footer-rule::after { content: ""; position: absolute; right: 0; top: 0; width: 40%; height: 3px; background: var(--green); }

  .label { left: 696px; width: 132px; }
  .label.top { top: 38px; height: 77px; }
  .label.bottom { top: 175px; height: 82px; }
  .label .wordmark { position: absolute; left: 8px; top: 9px; font-size: 9px; }
  .label .contact { position: absolute; left: 8px; top: 21px; }
  .label .footer-rule { position: absolute; left: 0; right: 0; bottom: 0; height: 4px; background: var(--blue); }

  .envelope-back { left: 955px; top: 65px; width: 235px; height: 93px; background: var(--green); }
  .envelope-back svg { position: absolute; inset: 0; }
  .envelope-mid { left: 876px; top: 98px; width: 276px; height: 94px; }
  .envelope-mid .wordmark { position: absolute; left: 12px; top: 12px; font-size: 11px; color: var(--blue); }
  .envelope-mid .band { position: absolute; left: 0; right: 0; bottom: 0; height: 6px; background: var(--green); }
  .envelope-front { left: 876px; top: 202px; width: 300px; height: 81px; }
  .envelope-front .wordmark { position: absolute; left: 12px; top: 10px; font-size: 11px; }
  .envelope-front .contact { position: absolute; left: 12px; top: 23px; }
  .envelope-front .footer-rule { position: absolute; left: 0; right: 0; bottom: 0; height: 4px; background: var(--blue); }
</style>
</head>
<body>
  <div class="brand-block">
    <div class="wordmark">DERFINCO</div>
    <div class="tagline">Smart Home Lending</div>
  </div>

  <div class="piece card-wide">
    <div class="wordmark">DERFINCO</div>
    <div class="stripe"></div>
  </div>
  <div class="caption" style="left:19px;top:158px">Business Card Back</div>

  <div class="piece card-front">
    <div class="wordmark">DERFINCO</div>
    <div class="person contact">
      <strong>Mark T. Derrow</strong>
      President<br>
      418 Welland Avenue Palo Alto, CA 94306<br>
      mark@derfinco.com · derfinco.com<br>
      CA DRE: #00461738, NMLS: #517264
    </div>
    <div class="mark-dot"></div>
  </div>
  <div class="caption" style="left:19px;top:261px">Business Card Front</div>

  <div class="piece card-back">
    <div class="wordmark on-blue">DERFINCO</div>
  </div>

  <div class="piece letterhead one">
    <div class="wordmark">DERFINCO</div>
    <div class="contact">418 Welland Avenue<br>Palo Alto, CA 94306<br>derfinco.com</div>
    <div class="watermark"></div>
    <div class="footer-rule"></div>
  </div>
  <div class="caption" style="left:264px;top:278px">Letterhead Page One</div>

  <div class="piece letterhead two">
    <div class="wordmark">DERFINCO</div>
    <div class="watermark"></div>
    <div class="footer-rule"></div>
  </div>
  <div class="caption" style="left:480px;top:278px">Letterhead Page Two</div>

  <div class="piece label top">
    <div class="wordmark">DERFINCO</div>
    <div class="contact">418 Welland Avenue<br>Palo Alto, CA 94306</div>
    <div class="footer-rule"></div>
  </div>
  <div class="caption" style="left:696px;top:119px">Mailing Label</div>

  <div class="piece label bottom">
    <div class="wordmark">DERFINCO</div>
    <div class="contact">418 Welland Avenue<br>Palo Alto, CA 94306</div>
    <div class="footer-rule"></div>
  </div>
  <div class="caption" style="left:696px;top:261px">Mailing Label</div>

  <div class="piece envelope-back">
    <svg width="235" height="93" viewBox="0 0 235 93">
      <polygon points="0,0 235,0 117,48" fill="var(--green-dark)"/>
    </svg>
  </div>
  <div class="caption" style="left:1120px;top:55px">Envelope Back</div>

  <div class="piece envelope-mid">
    <div class="wordmark">DERFINCO</div>
    <div class="band"></div>
  </div>

  <div class="piece envelope-front">
    <div class="wordmark">DERFINCO</div>
    <div class="contact">418 Welland Avenue<br>Palo Alto, CA 94306</div>
    <div class="footer-rule"></div>
  </div>
  <div class="caption" style="left:1120px;top:288px">Envelope Front</div>
</body>
</html>
```